Startup online payment business - Sporting / Golf, Swift Tee payment

Background:
Our business name is "Swift Tee" we provide online payments for golfing services via our website. We currently have a logo used on our website. No other design style has been developed. Our aim is to remove cash payments for service at golf clubs.

Our Key Values:
Quick and easy
Formal and polite
Fun with professional boundary
Mate-ship relationships
100% online digital

What we want from you:
Marketing design to be used on posters and stickers in a retail setting to direct customers to our online payment Chanel.
Design must incorporate attached logo, URL swifttee.com.au and our key values can act as a guide the type of design. We have used color Hex#007672 for logo background. We are open to use other colors.

Target Market(s)

Golf clubs and golf players

Industry/Entity Type

Golf Course

Font styles to use
Sans Serif

Requirements
Must have
• Directions to online payment via URL: swifttee.com.au
Nice to have
• We like the idea of the slogan: No Cash - No worries. Have attached home screen that will be available from URL link. Consideration if using mobile phone in image. Push the online payment and steps 1. Visit swifttee.com 2. Select club 3. Confirm payment
Should not have
• Cartoons

```html
<!DOCTYPE html>
<html lang="en">
<head>
<meta charset="utf-8">
<title>Swift Tee – No Cash No Worries Poster</title>
<link rel="stylesheet" href="https://fonts.googleapis.com/css2?family=Bebas+Neue&family=Rubik:wght@400;500;700&display=swap">
<style>
  :root{
    --teal:#007672;
    --teal-dark:#0a3f47;
    --navy:#0d2a36;
    --charcoal:#333538;
    --slate:#4a4f57;
    --ink:#2b2b2b;
    --white:#ffffff;
    --photo-a:#3d5f78;
    --photo-b:#7a5a62;
    --photo-c:#26445a;
  }
  *{box-sizing:border-box;margin:0;padding:0}
  html,body{width:915px;height:1200px;overflow:hidden;background:#d4d4d4}
  body{font-family:"Rubik",Arial,sans-serif;color:var(--ink)}
  .poster{position:relative;width:915px;height:1200px;background:var(--white);overflow:hidden}

  /* hero */
  .hero-photo{position:absolute;left:0;top:0;width:915px;height:719px;
    background:
      radial-gradient(ellipse at 30% 18%, var(--photo-b) 0%, transparent 45%),
      radial-gradient(ellipse at 85% 60%, #c99a86 0%, transparent 30%),
      linear-gradient(160deg, var(--photo-a) 0%, var(--photo-c) 60%, #1c3444 100%);}
  .brand-box{position:absolute;left:43px;top:0;width:327px;height:279px;background:var(--teal);
    display:flex;align-items:center;justify-content:center}
  .brand-name{font-family:"Rubik",Arial,sans-serif;font-weight:700;color:var(--white);font-size:46px;letter-spacing:1px}
  .slogan{position:absolute;left:44px;font-family:"Bebas Neue",Impact,sans-serif;color:var(--white);
    font-size:142px;line-height:1;letter-spacing:-2px;white-space:nowrap}
  .slogan.line-1{top:294px}
  .slogan.line-2{top:412px}

  .intro-band{position:absolute;left:0;top:564px;width:573px;height:155px}
  .intro-band svg{position:absolute;inset:0}
  .intro-text{position:absolute;left:40px;font-size:20.5px;color:var(--white);line-height:1.25;font-weight:400}
  .intro-text b{font-weight:700}
  .intro-text.first{top:14px}
  .intro-text.second{top:82px}

  /* app screen */
  .app-screen{position:absolute;left:586px;top:127px;width:292px;height:479px;background:var(--teal);
    color:var(--white);box-shadow:0 0 0 1px rgba(0,0,0,.15)}
  .app-screen > *{position:absolute}
  .app-login{left:9px;top:15px;width:39px;height:20px;border:1px solid var(--white);border-radius:5px;
    font-size:8px;display:flex;align-items:center;justify-content:center}
  .app-menu{right:12px;top:11px;width:25px;height:28px;border:1px solid var(--white);border-radius:3px;
    display:flex;align-items:center;justify-content:center}
  .app-brand{left:0;right:0;top:44px;text-align:center;font-weight:700;font-size:24px}
  .app-welcome{left:18px;top:114px;font-size:14px;border-bottom:1px solid var(--white);padding-right:4px}
  .app-note{left:18px;top:150px;width:240px;font-size:9px;line-height:1.4}
  .app-label{left:18px;font-size:13.5px}
  .app-label.club{top:196px}
  .app-label.players{top:282px}
  .app-search{left:20px;top:237px;width:242px;height:27px;background:var(--white);border:3px solid #e7eaee;
    display:flex;align-items:center;padding-left:30px;gap:8px;color:#7a8594;font-size:9.5px}
  .app-stepper{left:20px;top:318px;display:flex;align-items:center;gap:8px}
  .stepper-btns{display:flex;border:2px solid var(--charcoal);border-radius:3px;overflow:hidden}
  .stepper-btns span{width:35px;height:22px;display:flex;align-items:center;justify-content:center;
    color:var(--charcoal);font-size:18px;font-weight:500;background:var(--teal)}
  .stepper-btns span + span{border-left:2px solid var(--charcoal)}
  .stepper-value{width:45px;height:24px;background:var(--white);color:var(--ink);font-size:9px;
    display:flex;align-items:center;justify-content:center}
  .app-holes{left:175px;top:320px;display:flex;align-items:center;gap:10px;font-size:8px}
  .toggle{width:38px;height:20px;border-radius:10px;background:var(--white);box-shadow:inset 0 0 0 1px #ccc}
  .app-total{left:20px;top:364px;font-size:14px}
  .app-submit{left:20px;top:400px;width:242px;height:35px;background:var(--slate);border-radius:3px;
    font-size:11px;display:flex;align-items:center;justify-content:center}
  .app-dots{left:0;right:0;top:447px;text-align:center;font-size:10px;letter-spacing:3px;opacity:.85}

  /* key values */
  .section-title{font-family:"Bebas Neue",Impact,sans-serif;color:var(--white);line-height:.95;font-weight:400}
  .values-head{position:absolute;left:0;top:728px;width:352px;height:61px;background:var(--teal);
    border-radius:0 31px 31px 0;padding:6px 0 0 31px;font-size:52px}
  .values-list{position:absolute;left:31px;top:804px;list-style:none}
  .values-list li{display:flex;align-items:flex-start;gap:12px;font-size:28px;font-weight:500;
    line-height:1.12;color:#333;margin-bottom:21px}
  .values-list li:nth-child(3){margin-bottom:21px}
  .values-list svg{flex:none;margin-top:4px}
  .divider{position:absolute;left:467px;top:722px;width:4px;height:406px;background:var(--teal)}

  /* steps */
  .steps-head{position:absolute;left:471px;top:728px;width:444px;height:110px;background:var(--teal);
    padding:10px 0 0 14px;font-size:49px}
  .step{position:absolute;left:496px;display:flex;align-items:center;gap:18px}
  .step-num{width:66px;height:66px;border-radius:50%;background:var(--teal);
    box-shadow:0 0 0 3px var(--white),0 0 0 5px var(--teal);color:var(--white);
    font-weight:700;font-size:52px;display:flex;align-items:center;justify-content:center}
  .step-text{font-weight:700;font-size:21px;line-height:1.1;color:var(--ink)}
  .step-text em{font-style:normal;color:var(--teal)}
  .step.one{top:865px}
  .step.two{top:951px}
  .step.three{top:1034px}
  .step-rule{position:absolute;left:575px;width:187px;height:1px;background:var(--teal)}

  /* footer */
  .footer{position:absolute;left:0;top:1128px;width:915px;height:72px;background:var(--charcoal)}
  .footer svg{position:absolute;left:0;top:0}
  .footer-text{position:absolute;left:0;right:0;top:10px;text-align:center;color:var(--white);
    font-weight:700;font-size:15px;white-space:nowrap}
  .footer-text strong{font-size:29px;letter-spacing:.5px;vertical-align:-3px;margin-left:4px}
</style>
</head>
<body>
<main class="poster">

  <section class="hero">
    <div class="hero-photo" role="img" aria-label="Blurred photo of a smiling golfer holding out a smartphone towards the viewer"></div>

    <div class="brand-box"><span class="brand-name">Swift Tee</span></div>

    <h1>
      <span class="slogan line-1">NO CASH</span>
      <span class="slogan line-2">NO WORRIES</span>
    </h1>

    <div class="app-screen" aria-label="Swift Tee payment home screen">
      <span class="app-login">Login</span>
      <span class="app-menu">
        <svg width="11" height="9" viewBox="0 0 11 9"><path d="M0 1h11M0 4.5h11M0 8h11" stroke="#fff" stroke-width="1.4"/></svg>
      </span>
      <span class="app-brand">Swift Tee</span>
      <span class="app-welcome">Welcome to Swift Tee.</span>
      <p class="app-note">You can pay your Swift Tee fees for participating clubs here.</p>
      <span class="app-label club">Choose your Club</span>
      <div class="app-search">
        <svg width="10" height="10" viewBox="0 0 10 10"><circle cx="4" cy="4" r="3.2" fill="none" stroke="#7a8594" stroke-width="1"/><path d="M6.4 6.4 9.5 9.5" stroke="#7a8594" stroke-width="1"/></svg>
        Type the Name of your Club
      </div>
      <span class="app-label players">How many Players and Holes</span>
      <div class="app-stepper">
        <div class="stepper-btns"><span>−</span><span>+</span></div>
        <span class="stepper-value">4</span>
      </div>
      <div class="app-holes"><span>9</span><span class="toggle"></span><span>18</span></div>
      <span class="app-total">Greens Total:&nbsp; $15.00</span>
      <span class="app-submit">Submit</span>
      <span class="app-dots">● ● ● ●</span>
    </div>

    <div class="intro-band">
      <svg width="573" height="155" viewBox="0 0 573 155" aria-hidden="true">
        <defs>
          <linearGradient id="bandFill" x1="0" y1="0" x2="1" y2="0">
            <stop offset="0" stop-color="#0b2f3c"/>
            <stop offset="1" stop-color="#0d4f55"/>
          </linearGradient>
        </defs>
        <polygon points="0,0 463,0 573,155 0,155" fill="url(#bandFill)"/>
      </svg>
      <p class="intro-text first">We provide online <b>payments for<br>golfing services via our website.</b></p>
      <p class="intro-text second">Our aim is to <b>remove cash payments<br>for service at golf clubs.</b></p>
    </div>
  </section>

  <section class="values">
    <h2 class="section-title values-head">OUR KEY VALUES</h2>
    <ul class="values-list">
      <li><svg width="24" height="24" viewBox="0 0 24 24"><circle cx="12" cy="12" r="10" fill="none" stroke="#007672" stroke-width="2.4"/><path d="M7 12.3l3.3 3.2L17 8.8" fill="none" stroke="#007672" stroke-width="2.4"/></svg>Quick and easy</li>
      <li><svg width="24" height="24" viewBox="0 0 24 24"><circle cx="12" cy="12" r="10" fill="none" stroke="#007672" stroke-width="2.4"/><path d="M7 12.3l3.3 3.2L17 8.8" fill="none" stroke="#007672" stroke-width="2.4"/></svg>Formal and polite</li>
      <li><svg width="24" height="24" viewBox="0 0 24 24"><circle cx="12" cy="12" r="10" fill="none" stroke="#007672" stroke-width="2.4"/><path d="M7 12.3l3.3 3.2L17 8.8" fill="none" stroke="#007672" stroke-width="2.4"/></svg>Fun with professional<br>boundary</li>
      <li><svg width="24" height="24" viewBox="0 0 24 24"><circle cx="12" cy="12" r="10" fill="none" stroke="#007672" stroke-width="2.4"/><path d="M7 12.3l3.3 3.2L17 8.8" fill="none" stroke="#007672" stroke-width="2.4"/></svg>Mate-ship relationships</li>
      <li><svg width="24" height="24" viewBox="0 0 24 24"><circle cx="12" cy="12" r="10" fill="none" stroke="#007672" stroke-width="2.4"/><path d="M7 12.3l3.3 3.2L17 8.8" fill="none" stroke="#007672" stroke-width="2.4"/></svg>100% online digital</li>
    </ul>
  </section>

  <div class="divider"></div>

  <section class="steps">
    <h2 class="section-title steps-head">PUSH THE ONLINE<br>PAYMENT AND STEPS</h2>
    <div class="step one"><span class="step-num">1</span><p class="step-text">VISIT AT<br><em>SWIFTTEE.COM</em></p></div>
    <div class="step-rule" style="top:940px"></div>
    <div class="step two"><span class="step-num">2</span><p class="step-text">SELECT <em>CLUB</em></p></div>
    <div class="step-rule" style="top:1021px"></div>
    <div class="step three"><span class="step-num">3</span><p class="step-text">CONFIRM<br><em>PAYMENT</em></p></div>
  </section>

  <footer class="footer">
    <svg width="915" height="72" viewBox="0 0 915 72" aria-hidden="true">
      <polygon points="36,0 887,0 866,59 57,59" fill="#007672"/>
    </svg>
    <p class="footer-text">Directions to online payment via URL: <strong>WWW.SWIFTTEE.COM.AU</strong></p>
  </footer>

</main>
</body>
</html>
```